General Dental Office Business Card

I run a private general dental office in southern California, and would like a refresh/redesign of my business card. I focus on quality care rather than volume. The email address on the uploaded current card should be updated to: info@marbleshoredental.example. The current card's logo is a deboss, but I am open to other ideas. The logo can be refreshed, but it is something that's been with me since the beginning of the office, so I wouldn't want a drastic redesign.
Target Market(s)
Adults 18-99, whoever needs dental services
Industry/Entity Type
Healthcare/Dental
Contact Information for Business Card
Name, Address, Phone, email
Colors
Designer to choose colors to be used in the design.
Requirements
Must have
- Logo (Same as original one in the uploaded file), space on back for appointment time/date

```html
<!DOCTYPE html>
<html lang="en">
<head>
<meta charset="utf-8">
<title>Marble Shore Dental – Business Card</title>
<link href="https://fonts.googleapis.com/css2?family=Montserrat:wght@400;500;600;700&display=swap" rel="stylesheet">
<style>
  :root {
    --accent: #8dd3ec;
    --accent-band: #a9def1;
    --ink: #1f1f1f;
    --rule: #4a4a4a;
    --paper: #ffffff;
    --backdrop: #e6e5e6;
    --watermark: #f3f9fc;
  }
  * { box-sizing: border-box; margin: 0; padding: 0; }
  html, body {
    width: 1200px; height: 1108px; overflow: hidden;
    background: var(--backdrop);
    font-family: "Montserrat", sans-serif;
    color: var(--ink);
  }
  .card {
    position: absolute;
    width: 729px; height: 436px;
    background: var(--paper);
    overflow: hidden;
  }
  .card--front { left: 237px; top: 67px; }
  .card--back  { left: 244px; top: 580px; }
  .card > * { position: absolute; }

  .watermark {
    border-radius: 50%;
    background: var(--watermark);
  }
  .card--front .watermark { left: 5px; top: 95px; width: 310px; height: 310px; }
  .card--back .watermark { left: 195px; top: 20px; width: 390px; height: 390px; }

  .bottom-band {
    left: 0; right: 0; bottom: 0; height: 30px;
    background: linear-gradient(to bottom, #d8f0f9, var(--accent-band));
  }

  .brand-name {
    left: 397px; top: 74px; width: 300px;
    text-align: center;
    font-size: 27px; font-weight: 500;
    color: var(--accent);
    letter-spacing: 0.3px;
  }

  .dentist-name {
    left: 27px; top: 183px;
    font-size: 27px; font-weight: 700;
    color: var(--accent);
  }
  .dentist-role { left: 28px; top: 220px; font-size: 15px; }
  .divider {
    left: 27px; top: 252px; width: 672px; height: 1px;
    background: var(--accent);
  }

  .contact-list { left: 30px; top: 299px; list-style: none; }
  .contact-list li {
    display: flex; align-items: center;
    height: 33px; font-size: 15.5px;
  }
  .contact-list svg { width: 20px; height: 20px; margin-right: 12px; fill: var(--accent); }

  .address {
    left: 518px; top: 342px;
    font-size: 16px; line-height: 20px; font-style: normal;
  }

  .appointment-title {
    left: 0; right: 0; top: 55px; text-align: center;
    font-size: 23px; font-weight: 500; color: var(--accent);
  }
  .appointment-sub {
    left: 0; right: 0; top: 96px; text-align: center;
    font-size: 16px;
  }
  .field-label { font-size: 16px; }
  .field-line { height: 2px; background: var(--rule); }
  .label-name { left: 33px; top: 186px; }
  .line-name  { left: 100px; top: 201px; width: 586px; }
  .label-date { left: 33px; top: 259px; }
  .line-date  { left: 94px; top: 272px; width: 270px; }
  .label-time { left: 374px; top: 259px; }
  .line-time  { left: 432px; top: 272px; width: 258px; }
  .notice {
    left: 0; right: 0; top: 357px; text-align: center;
    font-size: 16px;
  }
</style>
</head>
<body>

<section class="card card--front" aria-label="Business card front">
  <div class="watermark" role="img" aria-label="Faint palm tree emblem decoration"></div>
  <div class="brand-name">Marble Shore Dental</div>

  <h1 class="dentist-name">Daniel R. Soto DDS</h1>
  <p class="dentist-role">General Dentistry</p>
  <div class="divider"></div>

  <ul class="contact-list">
    <li>
      <svg viewBox="0 0 20 20" aria-hidden="true"><path d="M2 7c0-2 4-3.5 8-3.5S18 5 18 7v1.5h-4V7H6v1.5H2z"/><path d="M5 10h10l1 7H4z"/><circle cx="10" cy="13.5" r="2" fill="#fff"/></svg>
      949-555-0142
    </li>
    <li>
      <svg viewBox="0 0 20 20" aria-hidden="true"><path d="M2 5h16v10H2z"/><path d="M2 5l8 6 8-6" fill="none" stroke="#fff" stroke-width="1.4"/></svg>
      info@marbleshoredental.example
    </li>
    <li>
      <svg viewBox="0 0 20 20" aria-hidden="true"><circle cx="10" cy="10" r="8"/><path d="M6 6c2 0 3 1 2 3s1 3 0 5M12 4c0 2 2 2 3 3M13 12c1 0 2 1 1 3" fill="none" stroke="#fff" stroke-width="1.3"/></svg>
      www.marbleshoredental.example
    </li>
  </ul>

  <address class="address">1280 Harbor Crest Way<br>Coral Bay, CA 92000</address>

  <div class="bottom-band"></div>
</section>

<section class="card card--back" aria-label="Business card back">
  <div class="watermark" role="img" aria-label="Faint palm tree emblem decoration"></div>

  <h2 class="appointment-title">YOUR NEXT APOINMENT</h2>
  <p class="appointment-sub">Adults 18-99, whoever needs dental services</p>

  <span class="field-label label-name">NAME:</span>
  <div class="field-line line-name"></div>
  <span class="field-label label-date">DATE:</span>
  <div class="field-line line-date"></div>
  <span class="field-label label-time">TIME:</span>
  <div class="field-line line-time"></div>

  <p class="notice">if unable to keep this apoinment please kindly give 24hrs notice</p>

  <div class="bottom-band"></div>
</section>

</body>
</html>
```